Medical Device Company needs website

We are a start-up medical device company looking to sell boot (foot) and brace (ankle) products on Shopify. We are still working on the name but you can use Kaltir as a placeholder- no logo yet)

Website information:
- Look: modern/tech with clean lines and symmetry.
- Colors: teal, white, black, and greys.
- Headers: home, shop, about us, help, blog
- Icons (upper right): search, my account and shopping cart
-place to sign up for newsletter

```html
<!DOCTYPE html>
<html lang="en">
<head>
<meta charset="utf-8">
<title>Kaltir — Ankle &amp; Foot Care</title>
<link rel="stylesheet" href="https://fonts.googleapis.com/css2?family=Outfit:wght@300;400;500;600;700&family=Tinos:wght@400;700&display=swap">
<style>
:root{
  --teal:#0e7c7b;
  --teal-dark:#0a6867;
  --teal-soft:#7fc6c5;
  --ink:#111111;
  --text:#444444;
  --muted:#666666;
  --grey-bg:#f1f2f4;
  --hero-bg:#e4e6e9;
  --line:#e2e2e2;
  --white:#ffffff;
  --black:#000000;
}
*{box-sizing:border-box;margin:0;padding:0}
html,body{width:1200px;height:4739px;overflow:hidden}
body{font-family:"Outfit",sans-serif;color:var(--text);background:var(--white);position:relative}
section,header,nav,footer{position:relative;width:1200px;display:block}
.abs{position:absolute}
.btn{display:inline-block;background:var(--teal);color:var(--white);font-weight:600;font-size:16px;padding:0 22px;height:44px;line-height:44px;border-radius:2px}
.section-title{font-size:30px;font-weight:700;color:var(--ink);text-align:center;letter-spacing:.2px}
.section-lead{font-size:14.5px;line-height:30px;color:var(--text);text-align:center}

/* top bar */
.topbar{height:42px;background:var(--teal);color:var(--white)}
.topbar .welcome{left:112px;top:12px;font-size:14px;font-weight:600}
.topbar .social{right:112px;top:14px;display:flex;gap:14px}
.dot{width:13px;height:13px;border-radius:50%;background:var(--white);display:block}

/* nav */
.nav{height:85px;background:var(--white)}
.brand{left:110px;top:24px;font-size:29px;font-weight:700;color:var(--ink);letter-spacing:.5px}
.menu{left:397px;top:33px;display:flex;gap:42px;font-size:14.5px;font-weight:500;color:var(--ink);list-style:none}
.menu .active{color:var(--teal);border-bottom:2px solid var(--teal);padding-bottom:4px}
.tools{left:974px;top:30px;display:flex;gap:24px;align-items:center}
.cart{position:relative}
.cart .count{position:absolute;right:-9px;top:-8px;width:16px;height:16px;border-radius:50%;background:var(--teal);color:var(--white);font-size:10px;text-align:center;line-height:16px}

/* hero */
.hero{height:523px;background:linear-gradient(90deg,#f0f1f3 0%,#e6e8eb 60%,#dde0e4 100%)}
.hero h1{left:110px;top:115px;font-size:43px;line-height:52px;font-weight:700;color:var(--ink)}
.hero h1 span{color:var(--teal)}
.hero p{left:110px;top:232px;width:470px;font-size:16px;line-height:30px;color:var(--text)}
.hero .btn{left:110px;top:310px}
.hero .product-photo{left:570px;top:145px;width:570px;height:205px;border-radius:50%;background:radial-gradient(ellipse at center,#b7cfd8 0%,#8fb6c7 45%,rgba(220,224,228,0) 72%)}
.dots{display:flex;gap:10px}
.dots i{width:12px;height:12px;border-radius:50%;background:var(--teal-soft);display:block}
.dots i.on{background:var(--teal)}
.hero .dots{left:573px;top:425px}

/* why */
.why{height:906px}
.why .section-title{position:absolute;left:0;width:100%;top:100px}
.why .section-lead{position:absolute;left:150px;width:900px;top:155px}
.features{left:110px;top:238px;display:grid;grid-template-columns:repeat(3,314px);gap:20px 18px}
.feature{height:287px;background:var(--white);box-shadow:0 0 8px rgba(0,0,0,.14);text-align:center;padding-top:40px}
.feature .icon{width:84px;height:66px;margin:0 auto;background:var(--teal)}
.feature h3{margin-top:31px;font-size:14.5px;font-weight:600;color:var(--teal)}
.feature p{margin:14px auto 0;width:290px;font-size:14px;line-height:28px;color:var(--text)}

/* about */
.about{height:574px;background:radial-gradient(circle at 15% 30%,#eef0f2 0%,#f3f4f6 60%,#eef0f2 100%)}
.about .photo{left:110px;top:91px;width:470px;height:396px;border-radius:10px;background:linear-gradient(135deg,#b7bcc2 0%,#8e9ba6 45%,#5e7a94 100%)}
.about h2{left:632px;top:90px;font-size:30px;font-weight:700;color:var(--ink)}
.about .body{left:632px;top:148px;width:460px;font-size:14.5px;line-height:30px;color:var(--text)}
.about .body p+p{margin-top:30px}
.about .btn{left:632px;top:420px}

/* products */
.products{height:738px}
.products .section-title{position:absolute;left:0;width:100%;top:92px}
.products .section-lead{position:absolute;left:140px;width:920px;top:140px}
.tabs{left:312px;top:220px;display:flex;gap:27px}
.tab{width:174px;height:50px;border:2px solid var(--teal);color:var(--teal);font-size:16px;font-weight:600;text-align:center;line-height:46px;border-radius:2px}
.tab.on{background:var(--teal);color:var(--white)}
.cards{left:110px;top:323px;display:flex;gap:26px}
.card{width:309px;text-align:center}
.card .thumb{height:245px;border-radius:10px;background:var(--white);box-shadow:0 0 10px rgba(0,0,0,.13);display:flex;align-items:center;justify-content:center}
.card .thumb span{width:160px;height:160px;border-radius:12px;display:block}
.card h4{margin-top:20px;font-size:18px;font-weight:600;color:var(--ink)}
.card .price{margin-top:8px;font-size:18px;font-weight:600;color:var(--teal)}
.arrow{top:430px}

/* testimonials */
.testimonials{height:624px}
.testimonials .band{left:0;top:0;width:1200px;height:370px;background:linear-gradient(120deg,#0e7c7b 0%,#0e7c7b 70%,#137f7e 85%,#0b7271 100%)}
.testimonials h2{left:0;width:100%;top:70px;text-align:center;font-size:32px;font-weight:700;color:var(--white)}
.testimonials .lead{left:200px;width:800px;top:124px;text-align:center;font-size:16px;line-height:30px;color:var(--white)}
.quote-card{left:232px;top:259px;width:736px;height:263px;background:var(--white);border-radius:10px;box-shadow:0 4px 14px rgba(0,0,0,.12);text-align:center}
.quote-card q{display:block;margin:78px auto 0;width:590px;font-size:16px;line-height:30px;color:var(--text)}
.quote-card .name{margin-top:20px;font-size:15px;font-weight:600;color:var(--ink)}
.quote-card .dots{justify-content:center;margin-top:18px}
.quote-card .dots i{background:var(--white);border:2px solid var(--teal)}
.quote-card .dots i.on{background:var(--teal)}
.avatar{left:543px;top:206px;width:114px;height:93px;background:var(--white);padding:5px;box-shadow:0 0 8px rgba(0,0,0,.15)}
.avatar span{display:block;width:100%;height:100%;background:linear-gradient(180deg,#c9d9dc,#5da1a8)}

/* blog */
.blog{height:458px}
.posts{left:108px;top:0;display:flex;gap:23px}
.post{width:311px}
.post .pic{height:228px}
.post time{display:block;margin-top:12px;font-size:12px;color:var(--ink)}
.post h5{margin-top:14px;width:290px;font-family:"Tinos",serif;font-weight:700;font-size:15px;line-height:24px;color:var(--ink)}
.post p{margin-top:10px;font-size:12.5px;line-height:23px;color:var(--ink);width:295px}

/* newsletter */
.newsletter{height:368px;background:var(--grey-bg)}
.newsletter h2{left:0;width:100%;top:72px;text-align:center;font-size:30px;font-weight:600;color:var(--ink);letter-spacing:1px}
.newsletter .lead{left:200px;width:800px;top:137px;text-align:center;font-size:16px;line-height:30px}
.signup{left:176px;top:237px;width:848px;height:55px;background:var(--white);border:1px solid #d0d0d0;display:flex;align-items:center;justify-content:space-between;padding:0 8px 0 24px}
.signup span{font-size:13px;color:#888}
.signup .btn{height:40px;line-height:40px;font-size:15px;padding:0 26px;color:var(--white)}

/* footer */
.footer{height:421px;background:var(--black);color:var(--white)}
.col{top:88px}
.col h6{font-size:24px;font-weight:600;margin-bottom:18px}
.col li{list-style:none;font-size:14.5px;line-height:31px}
.col p{font-size:13.5px;line-height:31px;width:260px}
.footer .social{display:flex;gap:22px;margin-top:18px}
.footer .rule{left:110px;top:379px;width:980px;height:1px;background:#444}
.footer .copy{left:0;width:100%;top:397px;text-align:center;font-size:13.5px}
</style>
</head>
<body>

<header class="topbar">
  <div class="abs welcome">WELCOME TO KALTIR</div>
  <div class="abs social" aria-label="Social links"><i class="dot"></i><i class="dot"></i><i class="dot"></i><i class="dot"></i></div>
</header>

<nav class="nav">
  <div class="abs brand">KALTIR</div>
  <ul class="abs menu">
    <li class="active">HOME</li><li>SHOP</li><li>ABOUT US</li><li>HELP</li><li>BLOG</li>
  </ul>
  <div class="abs tools">
    <svg width="20" height="20" viewBox="0 0 20 20" fill="none" stroke="#777" stroke-width="1.8" aria-label="Search"><circle cx="8.5" cy="8.5" r="6"/><path d="M13 13l5 5"/></svg>
    <svg width="22" height="22" viewBox="0 0 22 22" fill="none" stroke="#777" stroke-width="1.7" aria-label="My account"><circle cx="11" cy="11" r="3.2"/><circle cx="11" cy="11" r="7.5" stroke-dasharray="4 2.2"/></svg>
    <span class="cart"><svg width="22" height="24" viewBox="0 0 22 24" fill="none" stroke="#111" stroke-width="2" aria-label="Cart"><path d="M3 7h16l-1 15H4z"/><path d="M7 9V5a4 4 0 0 1 8 0v4"/></svg><span class="count">0</span></span>
  </div>
</nav>

<section class="hero">
  <h1 class="abs">TAKE CARE OF YOUR<br><span>ANKLE</span> HEALTH</h1>
  <p class="abs">Lorem ipsum dolor sit amet, consectetur adipiscing elit, do eiusmod tempor incididunt ut labore et dolore aliqua.</p>
  <span class="abs btn">SHOP NOW</span>
  <div class="abs product-photo" role="img" aria-label="Pair of blue and peach orthopedic insoles"></div>
  <div class="abs dots"><i></i><i class="on"></i><i></i></div>
</section>

<section class="why">
  <h2 class="section-title">WHY CHOOSE US</h2>
  <p class="section-lead">Lorem ipsum dolor sit amet, consectetur adipiscing elit, sed do eiusmod tempor incididunt ut labore et dolore magna aliqua.<br>Ut enim ad minim veniam, quis nostrud exercitation ullamco laboris nisi ut aliquip ex ea commodo consequat.</p>
  <div class="abs features">
    <article class="feature"><div class="icon" role="img" aria-label="Joint pain icon"></div><h3>NOSTRUD EXERCITATION ULLAMCO</h3><p>Excepteur sint occaecat cupidatat non proident, sunt in culpa qui officia deserunt mollit anim id est laborum.</p></article>
    <article class="feature"><div class="icon" role="img" aria-label="Knee joint icon"></div><h3>NOSTRUD EXERCITATION ULLAMCO</h3><p>Excepteur sint occaecat cupidatat non proident, sunt in culpa qui officia deserunt mollit anim id est laborum.</p></article>
    <article class="feature"><div class="icon" role="img" aria-label="Spine and back icon"></div><h3>NOSTRUD EXERCITATION ULLAMCO</h3><p>Excepteur sint occaecat cupidatat non proident, sunt in culpa qui officia deserunt mollit anim id est laborum.</p></article>
    <article class="feature"><div class="icon" role="img" aria-label="Hand therapy icon"></div><h3>NOSTRUD EXERCITATION ULLAMCO</h3><p>Excepteur sint occaecat cupidatat non proident, sunt in culpa qui officia deserunt mollit anim id est laborum.</p></article>
    <article class="feature"><div class="icon" role="img" aria-label="Leg massage icon"></div><h3>NOSTRUD EXERCITATION ULLAMCO</h3><p>Excepteur sint occaecat cupidatat non proident, sunt in culpa qui officia deserunt mollit anim id est laborum.</p></article>
    <article class="feature"><div class="icon" role="img" aria-label="Knee brace icon"></div><h3>NOSTRUD EXERCITATION ULLAMCO</h3><p>Excepteur sint occaecat cupidatat non proident, sunt in culpa qui officia deserunt mollit anim id est laborum.</p></article>
  </div>
</section>

<section class="about">
  <div class="abs photo" role="img" aria-label="Physiotherapist guiding an older patient through a resistance band exercise"></div>
  <h2 class="abs">ABOUT US</h2>
  <div class="abs body">
    <p>Lorem ipsum dolor sit amet, consectetur adipiscing elit, sed do eiusmod tempor incididunt ut labore et dolore magna aliqua. Ut enim ad minim veniam, quis nostrud exercitation ullamco laboris nisi ut aliquip ex ea commodo consequat.</p>
    <p>Duis aute irure dolor in reprehenderit in voluptate velit esse cillum dolore eu fugiat nulla pariatur. Excepteur sint occaecat cupidatat non proident, sunt in culpa qui officia deserunt mollit anim id est laborum.</p>
  </div>
  <span class="abs btn">SHOP NOW</span>
</section>

<section class="products">
  <h2 class="section-title">OUR PRODUCTS</h2>
  <p class="section-lead">Lorem ipsum dolor sit amet, consectetur adipiscing elit, sed do eiusmod tempor incididunt ut labore et dolore magna aliqua. Ut<br>enim ad minim veniam, quis nostrud exercitation ullamco laboris nisi ut aliquip ex ea commodo consequat.</p>
  <div class="abs tabs"><span class="tab on">NEW ARRIVALS</span><span class="tab">FEATURED</span><span class="tab">BEST SELLERS</span></div>
  <svg class="abs arrow" style="left:52px" width="14" height="26" viewBox="0 0 14 26" fill="none" stroke="#222" stroke-width="2"><path d="M12 2L2 13l10 11"/></svg>
  <svg class="abs arrow" style="left:1134px" width="14" height="26" viewBox="0 0 14 26" fill="none" stroke="#222" stroke-width="2"><path d="M2 2l10 11L2 24"/></svg>
  <div class="abs cards">
    <article class="card"><div class="thumb"><span role="img" aria-label="Grey walking boot" style="background:linear-gradient(160deg,#d9dbe0,#9fa4ae)"></span></div><h4>Lorem ipsum dolor</h4><div class="price">$ 45.00</div></article>
    <article class="card"><div class="thumb"><span role="img" aria-label="Orange ankle straps with buckles" style="background:linear-gradient(160deg,#f4b07a,#e77a2e)"></span></div><h4>Lorem ipsum dolor</h4><div class="price">$ 45.00</div></article>
    <article class="card"><div class="thumb"><span role="img" aria-label="Black massage gun" style="background:linear-gradient(160deg,#555,#151515)"></span></div><h4>Lorem ipsum dolor</h4><div class="price">$ 45.00</div></article>
  </div>
</section>

<section class="testimonials">
  <div class="abs band"></div>
  <h2 class="abs">TESTIMONIALS</h2>
  <p class="abs lead">Lorem ipsum dolor sit amet, consectetuer adipiscing elit. Aenean commodo ligula eget dolor. Aenean<br>massa. Cum sociis natoque penatibus Nullam quis ante</p>
  <div class="abs quote-card">
    <q>Lorem ipsum dolor sit amet, consectetur adipiscing elit, sed do eiusmod tempor incididunt ut labore et dolore magna aliqua.</q>
    <div class="name">MAREN</div>
    <div class="dots"><i></i><i class="on"></i><i></i></div>
  </div>
  <div class="abs avatar"><span role="img" aria-label="Portrait of a clinician in teal scrubs"></span></div>
</section>

<section class="blog">
  <div class="abs posts">
    <article class="post"><div class="pic" role="img" aria-label="Doctor holding a tablet with a spine scan" style="background:linear-gradient(135deg,#6a86a3,#c8d2dc)"></div><time>September 1, 2021</time><h5>Neque porro quisquam est, qui dolorem<br>ipsum quia</h5><p>At vero eos et accusamus et iusto odio dignissimos ducimus qui blanditiis praesentium voluptatum deleniti atque corrupti</p></article>
    <article class="post"><div class="pic" role="img" aria-label="Technician crafting an orthotic in a workshop" style="background:linear-gradient(135deg,#e6e2dd,#b0a9a3)"></div><time>September 1, 2021</time><h5>Neque porro quisquam est, qui dolorem<br>ipsum quia</h5><p>At vero eos et accusamus et iusto odio dignissimos ducimus qui blanditiis praesentium voluptatum deleniti atque corrupti</p></article>
    <article class="post"><div class="pic" role="img" aria-label="Therapist fitting a patient with a leg device" style="background:linear-gradient(135deg,#9bb0c8,#3a5fa0)"></div><time>September 1, 2021</time><h5>Neque porro quisquam est, qui dolorem<br>ipsum quia</h5><p>At vero eos et accusamus et iusto odio dignissimos ducimus qui blanditiis praesentium voluptatum deleniti atque corrupti</p></article>
  </div>
</section>

<section class="newsletter">
  <h2 class="abs">KALTIR</h2>
  <p class="abs lead">“Lorem ipsum dolor sit amet, consectetur adipiscing elit, sed do eiusmod tempor incididunt ut<br>labore et dolore magna aliqua.”</p>
  <div class="abs signup"><span>Your Email Address</span><span class="btn">Subscribe</span></div>
</section>

<footer class="footer">
  <div class="abs col" style="left:110px"><h6>About Us</h6><p>Lorem ipsum dolor sit amet,<br>consectetuer adipiscing elit, sed diam<br>nonummy nibh euismod tincidunt ut<br>laoreet dolore</p>
    <div class="social"><i class="dot"></i><i class="dot"></i><i class="dot"></i><i class="dot"></i><i class="dot"></i></div></div>
  <div class="abs col" style="left:427px"><h6>Information</h6><ul><li>Shipping</li><li>Returns</li><li>International</li><li>Privacy Policy</li><li>Conditions</li></ul></div>
  <div class="abs col" style="left:647px"><h6>Useful Links</h6><ul><li>Privacy Policy</li><li>Delivery Info</li><li>Credit Card</li><li>Careers</li><li>Contact Us</li></ul></div>
  <div class="abs col" style="left:867px"><h6>Contact Us</h6><ul><li>Office: 48 Harbor Lane, Westfield</li><li>Phone: (04) 55 6123 7788</li><li>Fax: 5550192837</li><li>Mail: hello@kaltirmail.com</li></ul></div>
  <div class="abs rule"></div>
  <div class="abs copy">Copyrights@2024.KALTIR.All Rights Reserved</div>
</footer>

</body>
</html>
```